Design for a Service-Based Estimate

We want a design for an Estimate that will always be sent in PDF format. The estimate or proposal is a critical document that needs to plainly show the service items, item description but also needs to be attractive and professional looking. Our current estimate deliverable is attached but it looks really basic like a Word document

```html
<!DOCTYPE html>
<html lang="en">
<head>
<meta charset="utf-8">
<title>Firmstone Paving – Invoice and Terms</title>
<link href="https://fonts.googleapis.com/css2?family=Poppins:wght@300;400;500;600;700&display=swap" rel="stylesheet">
<style>
  :root {
    --navy: #2f2d57;
    --orange: #d8462a;
    --ink: #2b2b3a;
    --rule: #b9b9c2;
    --paper: #ffffff;
    --backdrop: #3a3d42;
  }
  * { box-sizing: border-box; margin: 0; padding: 0; }
  html, body { width: 838px; height: 1200px; overflow: hidden; }
  body {
    background: var(--backdrop);
    font-family: "Poppins", sans-serif;
    color: var(--ink);
    position: relative;
  }
  .sheet {
    position: absolute;
    left: 199px;
    width: 440px;
    height: 569px;
    background: var(--paper);
    overflow: hidden;
    box-shadow: 0 4px 14px rgba(0,0,0,.35);
  }
  .sheet--invoice { top: 20px; }
  .sheet--terms { top: 611px; }
  .sheet__footer-band {
    position: absolute; left: 0; right: 0; bottom: 0; height: 14px;
    background: linear-gradient(90deg, var(--navy), var(--orange));
  }
  .brand {
    position: absolute;
    font-weight: 700;
    font-size: 17px;
    letter-spacing: 1px;
    color: var(--navy);
    white-space: nowrap;
  }
  .sheet--invoice .brand { top: 28px; left: 34px; }
  .sheet--terms .brand { top: 38px; left: 0; right: 0; text-align: center; }

  /* Invoice page */
  .doc-tab {
    position: absolute; top: 66px; right: 0;
    width: 122px; height: 72px;
    background: var(--orange);
    border-radius: 30px 0 0 30px;
    color: #fff; font-size: 25px; font-weight: 400;
    display: flex; align-items: center; justify-content: center;
    letter-spacing: .5px;
  }
  .bill-to { position: absolute; top: 74px; left: 34px; line-height: 1.25; }
  .bill-to__label { color: var(--orange); font-size: 8.5px; font-weight: 600; }
  .bill-to__name { color: var(--navy); font-size: 16px; font-weight: 300; }
  .bill-to__line { color: var(--ink); font-size: 8.5px; font-weight: 600; }
  .bill-to__email { font-weight: 400; }
  .project {
    position: absolute; top: 150px; left: 130px; width: 240px;
    text-align: center; color: var(--orange);
    font-size: 11.5px; font-weight: 700; line-height: 1.3;
  }
  .line-items {
    position: absolute; top: 208px; left: 0; width: 418px;
    border-collapse: collapse; font-size: 6.5px;
  }
  .line-items th {
    background: var(--navy); color: #fff; font-size: 8px; font-weight: 600;
    height: 26px; text-align: center;
  }
  .line-items th.col-item { text-align: left; padding-left: 20px; }
  .line-items td {
    border-right: 1px solid var(--rule);
    border-bottom: 1px solid var(--rule);
    text-align: center; vertical-align: middle; padding: 5px 4px;
  }
  .line-items td:last-child { border-right: none; }
  .line-items td.col-item { text-align: left; padding-left: 20px; width: 200px; line-height: 1.35; }
  .line-items .row-spacer td { height: 46px; border-bottom: none; }
  .line-items .optional { font-size: 7px; }
  .total-box {
    position: absolute; top: 330px; left: 300px; width: 118px; height: 30px;
    background: var(--navy); color: #fff;
    display: flex; align-items: center; justify-content: space-between;
    padding: 0 10px; font-size: 7px; font-weight: 500;
  }

  /* Terms page */
  .terms-title {
    position: absolute; top: 70px; left: 0; right: 0; text-align: center;
    color: var(--orange); font-size: 14px; font-weight: 700;
  }
  .terms-list {
    position: absolute; top: 104px; left: 40px; right: 36px;
    font-size: 6.6px; line-height: 1.45; padding-left: 10px;
  }
  .terms-list li { margin-bottom: 1px; }
  .signoff { position: absolute; width: 120px; }
  .signoff__rule { border-top: 1px solid #777; margin-bottom: 4px; }
  .signoff__label { color: var(--orange); font-size: 7.5px; font-weight: 600; }
  .signoff--client { top: 410px; left: 40px; }
  .signoff--date { top: 470px; right: 40px; }
</style>
</head>
<body>

<section class="sheet sheet--invoice">
  <div class="brand">FIRMSTONE PAVING</div>
  <div class="doc-tab">INVOICE</div>

  <div class="bill-to">
    <div class="bill-to__label">Invoice To:</div>
    <div class="bill-to__name">Dale Whitmore</div>
    <div class="bill-to__line">48 Harbor Lane Cedar Bay 30412</div>
    <div class="bill-to__line bill-to__email">dwhitmore@example.com</div>
  </div>

  <div class="project">
    Dale Whitmore New Concrete Pad<br>
    48 Harbor Lane Cedar Bay 30412<br>
    Bid#:20-0182
  </div>

  <table class="line-items">
    <thead>
      <tr>
        <th class="col-item">Item</th>
        <th>Quantity</th>
        <th>U/M</th>
        <th>Unit $</th>
        <th>Total $</th>
      </tr>
    </thead>
    <tbody>
      <tr>
        <td class="col-item">Form, Pour &amp; Finish New Concrete Slab (24' x 24' x 4"). Includes 3000psi Concrete Mix, Footer (12" x 8") with One (#5) Continuous Rebar, Wire Mesh Reinforcement and Saw-Cut Expansion Joints</td>
        <td>576</td><td>SF</td><td>$8.65</td><td>$4,982.40</td>
      </tr>
      <tr>
        <td class="col-item optional">OPTIONAL: Add (2' x 24' x 4") Small Ramp Area</td>
        <td>48</td><td>SF</td><td>$8.65</td><td>$415.20</td>
      </tr>
      <tr class="row-spacer">
        <td class="col-item"></td><td></td><td></td><td></td><td></td>
      </tr>
    </tbody>
  </table>

  <div class="total-box"><span>Total Price</span><span>$5,397.60</span></div>

  <div class="sheet__footer-band"></div>
</section>

<section class="sheet sheet--terms">
  <div class="brand">FIRMSTONE PAVING</div>
  <h1 class="terms-title">Terms and Condition</h1>

  <ul class="terms-list">
    <li>Price as quoted in this estimate are valid for (60) days oly.</li>
    <li>Payment in full, less any previously paid amounts, is due to the Contractor upon completion of the proposed scope of work.</li>
    <li>All change order requests must be communicated in writing to the Contractor by the Client or their authorized representative.</li>
    <li>All measurements listed in this estimate are approximate and may vary slightly due to actual field conditions.</li>
    <li>It is agreed by the Contractor and the Client that complications and costs arising from unforeseen conditions and handling of unsuitable materials are not included in this estimate.</li>
    <li>Unless specifically listed in this estimate the following items and their costs are not included: Maintenance of Traffic, Concrete Material Pumping, Testing, Excavation, Grading and Fill Material, Permits and Fees, Surveying and AS-builts, Irrigation Repair, Landscaping and Root Mitigation, De-watering, Private Locates and Accessibility.</li>
    <li>Private utility locating services using radio detection devices and, when necessary, ground penetrating radar are offered by Firmstone Paving to assist in finding private utilities that may not have been located by the public one call system. Firmstone Paving will not be responsible for private utilities that have not been located nor for the failure of the above equipment to accurately detect existing utilities since the equipment is fallible and existing site conditions may preclude the ability of the equipment to detect an identifiable signal.</li>
  </ul>

  <div class="signoff signoff--client">
    <div class="signoff__rule"></div>
    <div class="signoff__label">Client Signature</div>
  </div>
  <div class="signoff signoff--date">
    <div class="signoff__rule"></div>
    <div class="signoff__label">Date</div>
  </div>

  <div class="sheet__footer-band"></div>
</section>

</body>
</html>
```